Plakat-Design für IT-Systemhaus
brisk IT Solutions suchte ein neues Design in der Kategorie Plakate und hat ein Projekt auf grafikwerkhof.de gestartet.
brisk IT Solutions
The winner of our first design contests on this site. Can only say positive things about them. They work fast, respond in a timely manner and created a great design for us. Overall we're very happy with Quillwick.
Zielgruppe
Wir sind ein IT-Systemhaus mit dem Fokus auf individuelle Cloud Lösungen inkl. bester Kundenbetreuung.
Unsere primäre Zielgruppe sind Unterhnemenskunden, sprich das B2B Geschäft.
Aus der Gruppe der Unternehmenskunden interessieren uns besonders kleine und mittelständische Unternehmen.
Unser Corporate Design ist modern und dennoch auffällig gehalten.
Unsere bevorzugt Schriftart ist 'Ubuntu' bzw. 'Ubuntu Light'.
Unsere Grundfarben sind Orange (#ff8303) Grau (#747474).
Als orientierungshilfe haben wir unser Vorlage für Blöcke und Flyer mit angehangen.
Aufgabenstellung
Es handelt sich um eine Geländerwerbung (doppelseitig) zwischen einer Tankstelle und einer Straße gelegen. (Siehe Anhang)
Die Maße des Anzeitgetafel sind wie folgt: Querformat 135 x 65 (breite x höhe)
Gerne würden wir auf eine etwas provokantere Fragestellung zurückgreifen, um Aufmerksamkeit zu eregen.
Gleichzeitig möchten wir als Lösungsfinder der Fragestellung wargenommen werden.
Gut gefallen hat uns diese Lösung: https://www.grafikwerkhof.at/527190-plakat-fuer-it-systemhaus
Des Weiteren sollte die Anzeige unser Logo, Webadresse sowie unsere Telefonnummer enthalten.
Für Kreative Vorschläge sind wir dankbar.

```html
<!DOCTYPE html>
<html lang="de">
<head>
<meta charset="utf-8">
<title>brisk IT Solutions – Geländerbanner</title>
<link href="https://fonts.googleapis.com/css2?family=Ubuntu:wght@300;400;500;700&display=swap" rel="stylesheet">
<style>
  :root{
    --orange:#e8852e;
    --grey:#747474;
    --white:#ffffff;
    --stage:#e6e6e6;
    --photo-blue:#3b4f8c;
    --photo-violet:#6a5a8a;
    --photo-skin:#c98f78;
  }
  *{box-sizing:border-box;margin:0;padding:0}
  html,body{width:1200px;height:864px;overflow:hidden}
  body{background:var(--stage);font-family:'Ubuntu',sans-serif;position:relative}
  .banner{position:absolute;left:40px;top:162px;width:1120px;height:540px;background:var(--orange);overflow:hidden}
  .banner__photo{position:absolute;left:300px;top:0;width:820px;height:540px;
    background:
      radial-gradient(ellipse 260px 300px at 640px 260px, var(--photo-skin) 0%, rgba(201,143,120,.55) 45%, transparent 75%),
      linear-gradient(90deg, var(--orange) 0%, rgba(232,133,46,.6) 22%, var(--photo-violet) 45%, var(--photo-blue) 75%, #2c5fa8 100%);}
  .address{position:absolute;left:0;top:28px;width:420px;height:124px;
    border:2px solid rgba(255,255,255,.85);border-left:none;border-radius:0 62px 62px 0;
    display:flex;align-items:center;gap:14px;padding-left:30px;color:var(--white)}
  .address svg{width:24px;height:32px;flex:none;align-self:flex-start;margin-top:30px}
  .address__text{font-weight:700;font-size:25px;line-height:1.3}
  .headline{position:absolute;left:48px;top:262px;color:var(--white);
    font-weight:700;font-size:52px;line-height:1.1}
  .logo-field{position:absolute;left:0;top:400px;width:360px;height:140px;background:var(--white);
    clip-path:polygon(0 0,92% 0,100% 100%,0 100%);display:flex;align-items:center;padding-left:28px}
  .logo-field__name{font-weight:500;font-size:34px;color:var(--orange)}
  .services{position:absolute;left:365px;top:396px;display:flex;gap:10px;list-style:none}
  .services__tag{background:var(--orange);color:var(--white);font-weight:500;font-size:22px;padding:11px 17px;white-space:nowrap}
  .contact-phone{position:absolute;left:375px;top:462px;width:420px;height:62px;background:var(--white);
    display:flex;align-items:center;justify-content:center;color:var(--orange);font-weight:500;font-size:27px}
  .contact-web{position:absolute;left:795px;top:454px;width:305px;height:58px;background:var(--orange);
    display:flex;align-items:center;justify-content:center;color:var(--white);font-weight:500;font-size:24px}
</style>
</head>
<body>
  <section class="banner">
    <div class="banner__photo" role="img" aria-label="Foto: Hand steckt rote Netzwerkkabel in einen Switch im Serverschrank"></div>

    <div class="address">
      <svg viewBox="0 0 24 32" aria-hidden="true"><path d="M12 0C5.4 0 0 5.3 0 11.8 0 20.6 12 32 12 32s12-11.4 12-20.2C24 5.3 18.6 0 12 0zm0 16.5a4.8 4.8 0 1 1 0-9.6 4.8 4.8 0 0 1 0 9.6z" fill="#fff"/></svg>
      <p class="address__text">Lindenstraße 12 • 57318<br>Talbrück</p>
    </div>

    <h1 class="headline">Systeme sicher<br>vernetzen.</h1>

    <div class="logo-field"><span class="logo-field__name">brisk IT Solutions</span></div>

    <ul class="services">
      <li class="services__tag">IT Infrastruktur</li>
      <li class="services__tag">IT Support</li>
      <li class="services__tag">IT Sicherheit</li>
      <li class="services__tag">IT Beratung</li>
    </ul>

    <p class="contact-phone">Tel : +49 2800 / 13 57 24 0</p>
    <p class="contact-web">www.brisk-it.de</p>
  </section>
</body>
</html>
```